Ridgeline Throttle Touring Company needs brochure

We need a brochure for our motorcycle tour company, we run tours and provide other services like day rides, bespoke trips, heli taxis, trekking, mountain biking, white water rafting etc. We are a small company that runs the tours ourselves, providing excellent customer service . We are team of international friendly motorcycle enthusiasts with a passion for Nepal. With an office in the UK and in Nepal. Our brochure should reflect quality adventures, showcasing the Nepal Himalayas, our tours, and shout adventure. Target audience are Adventure Bikers. Below are some photos (all of which are owned by us, for use on our brochure only) Also the document with all the content for the brochure.

Target Market(s)

Adventure Motorbike Riders

Industry/Entity Type

Travel

Other font styles liked:
• Aurora for headings...

Requirements
Must have
• Adventure Feel. Looking cool and modern. Well thought out colour palette. Include big photos. Sometimes as background to text.
• touring in the himalayas:
Nice to have
• Infographics for the include exclude section.
• Want it to be A5 brochure, landscape, probably be needing 14 pages. Might make it shorter to 12 if possible.
• If you have access to vectors/graphics please use stuff related to Nepal like Buddhas eyes, stupas, prayer flags, bells, shiva trident, mountains, tyre tracks etc. Be imaginative and creative. I have uploaded a photo of rough layout but is quite open to interpretation. Need photos and text to be clear. Please let me know if any photos are not good quality.
Should not have
• It shouldn't look like a corporate brochure, boring,
• It shouldn't look like a Brokker Vantell type trip. We use adventure bikes.

```html
<!DOCTYPE html>
<html lang="en">
<head>
<meta charset="utf-8">
<title>Ridgeline Throttle Touring Company – Brochure</title>
<link rel="stylesheet" href="https://fonts.googleapis.com/css2?family=Exo+2:wght@300;400;600;700&family=Michroma&display=swap">
<style>
:root{
  --stage:#9b9b9b;
  --sky-deep:#1c86c6;
  --sky-mid:#4aa8dd;
  --sky-light:#8fd6f5;
  --sun:#f2fbff;
  --shadow:#0e1a26;
  --rock:#4a3d30;
  --band:rgba(28,28,32,.84);
  --paper:#f1f1f1;
  --paper-light:#fafafa;
  --ink:#2a2a2a;
  --ink-soft:#444;
  --red:#d3121b;
  --white:#ffffff;
  --map:#8e8e8e;
}
*{margin:0;padding:0;box-sizing:border-box}
html,body{width:1200px;height:1018px;overflow:hidden;background:var(--stage)}
.canvas{position:relative;width:1200px;height:1018px;font-family:"Exo 2",sans-serif;color:var(--ink)}
.spread{position:absolute;left:30px;width:1140px;height:401px;overflow:hidden}
.spread--cover{top:60px}
.spread--inner{top:557px;background:linear-gradient(115deg,var(--paper) 0%,var(--paper-light) 30%,#e9e9e9 48%,var(--paper-light) 62%,#ececec 100%)}
.spread__fold{position:absolute;left:569px;top:0;width:2px;height:100%;background:linear-gradient(90deg,rgba(0,0,0,.08),rgba(255,255,255,.4))}

/* cover */
.cover__photo{position:absolute;inset:0;background:
  radial-gradient(ellipse 24% 45% at 46% 72%,rgba(14,26,38,.92) 0%,rgba(14,26,38,.75) 45%,rgba(14,26,38,0) 100%),
  radial-gradient(ellipse 22% 38% at 72% 70%,rgba(14,26,38,.85) 0%,rgba(14,26,38,.6) 45%,rgba(14,26,38,0) 100%),
  radial-gradient(ellipse 12% 26% at 52% 22%,rgba(14,26,38,.7) 0%,rgba(14,26,38,0) 100%),
  radial-gradient(ellipse 30% 40% at 8% 100%,rgba(74,61,48,.95) 0%,rgba(74,61,48,.6) 50%,rgba(74,61,48,0) 100%),
  linear-gradient(180deg,rgba(0,0,0,0) 78%,rgba(30,30,30,.55) 100%),
  radial-gradient(circle at 43% 27%,var(--sun) 0%,var(--sky-light) 14%,var(--sky-mid) 38%,var(--sky-deep) 80%,#1978b4 100%)}
.cover__title{position:absolute;right:34px;top:40px;text-align:right;font-family:"Michroma",sans-serif;font-size:22px;line-height:33px;color:var(--white);letter-spacing:.3px}
.cover__band{position:absolute;left:0;right:0;top:340px;height:31px;background:var(--band)}
.cover__url{position:absolute;top:347px;font-family:"Exo 2",sans-serif;font-size:14px;letter-spacing:3.4px;color:var(--white)}
.cover__url b{font-weight:700}
.cover__url--left{left:52px}
.cover__url--right{right:48px}
.brand{position:absolute;top:191px;width:80px;height:80px;border-radius:50%;background:var(--red);display:flex;align-items:center;justify-content:center}
.brand span{font-family:"Exo 2",sans-serif;font-weight:700;font-size:9px;color:var(--white);letter-spacing:.8px;text-align:center;line-height:11px}
.brand--left{left:57px}
.brand--right{left:1026px}

/* inner */
.abs{position:absolute}
.heading{font-size:21px;font-weight:400;letter-spacing:-.3px;color:var(--ink)}
.heading strong{color:var(--red);font-weight:700}
.marker{width:0;height:0;border-top:8px solid var(--red);border-left:8px solid transparent}
.body{font-size:8.6px;line-height:10.4px;color:var(--ink-soft)}
.body--sm{font-size:7.4px;line-height:9.2px}
.sub{font-size:12.5px;color:var(--red);font-weight:400}
.sub--sm{font-size:9px;font-weight:600}
.red{color:var(--red)}
.red-b{color:var(--red);font-weight:700}
.map{position:absolute;left:308px;top:167px;width:200px;height:151px;border:1px solid #c9c9c9;background:var(--white);padding:4px}
.map div{width:100%;height:100%;background:linear-gradient(135deg,#d6d6d6 0%,var(--map) 45%,#6f6f6f 100%)}
.member{position:absolute;top:231px;width:56px;height:56px;border-radius:50%;border:2px solid #d9d9d9;background:linear-gradient(180deg,#9cc3e0 0%,#7a6a5a 100%)}
.member__name{position:absolute;top:292px;width:60px;text-align:center;font-size:9px;font-weight:600;color:var(--red)}
.bio{position:absolute;top:308px;width:147px;font-size:5.6px;line-height:7.1px;color:var(--ink-soft);text-align:justify}
</style>
</head>
<body>
<main class="canvas">

  <section class="spread spread--cover" aria-label="Brochure cover spread">
    <div class="cover__photo" role="img" aria-label="Photo of two young riders in full-face helmets with mountain bikes on a rocky ridge, silhouetted against a bright sunlit blue sky"></div>
    <div class="spread__fold"></div>
    <h1 class="cover__title">THE ULTIMATE<br>HIMALAYAN<br>MOTORCYCLE<br>ADVENTURE</h1>
    <div class="brand brand--left"><span>RIDGELINE<br>THROTTLE</span></div>
    <div class="brand brand--right"><span>RIDGELINE<br>THROTTLE</span></div>
    <div class="cover__band"></div>
    <p class="cover__url cover__url--left">www.<b>RidgelineThrottle</b>.example</p>
    <p class="cover__url cover__url--right">www.<b>RidgelineThrottle</b>.example</p>
  </section>

  <section class="spread spread--inner" aria-label="Contact and about spread">
    <div class="spread__fold"></div>

    <!-- where to find us -->
    <h2 class="heading abs" style="left:44px;top:34px">WHERE TO <strong>FIND US?</strong></h2>
    <div class="marker abs" style="left:44px;top:64px"></div>
    <p class="body abs" style="left:44px;top:85px;width:455px;font-size:11px;line-height:13px">With one foot in the UK and one foot in Nepal, we are ideally placed to organise your Himalayan adventures.</p>
    <h3 class="sub abs" style="left:44px;top:119px">Got a dream of travelling to the Himalayas?</h3>
    <p class="body abs" style="left:44px;top:137px;width:480px">I'll be your first contact right here in the UK to answer any questions regarding travelling to Nepal or Tibet. Don't hesitate to reach me via email or directly on my mobile.</p>
    <p class="abs" style="left:44px;top:167px;font-size:10.5px;color:var(--ink-soft)">Looking forward to hearing from you!</p>
    <p class="abs red-b" style="left:44px;top:188px;font-size:10px">Maren</p>
    <p class="body abs" style="left:44px;top:203px;font-size:9px"><span class="red">Mobile/ Messaging:</span> (+44)07700900412</p>
    <p class="body abs" style="left:44px;top:218px"><span class="red">Email:</span> maren@ridgelinethrottle.example</p>
    <h3 class="sub abs" style="left:44px;top:239px">Already in Kathmandu?</h3>
    <p class="body abs" style="left:44px;top:256px;width:246px">Come visit us at our office in Thamel Marg, 0km Kathmandu. You can rent one of our bikes for your own self guided tour or book a guided day ride if you want to experience the Himalayas by motorcycle but don't have much time.</p>
    <p class="body abs" style="left:44px;top:307px"><span class="red-b">Sujan or Hiroki</span> <span class="red">will be there to assist you.</span></p>
    <p class="body abs" style="left:44px;top:324px;font-size:9px"><span class="red">Mobile:</span> (+977)9841002233 <span class="red">Office:</span> (+977)014455120</p>
    <p class="body abs" style="left:44px;top:342px;width:470px">Check out our website for more details or find us on <span class="red">our social page (Ridgeline Throttle), photo feed (@ridgeline.throttle) and now on video channel (Ridgeline Throttle), like, follow and subscribe to our pages</span> for all our news and updates.</p>
    <div class="map"><div role="img" aria-label="Map of Europe and Asia marking the UK and Nepal offices"></div></div>

    <!-- about us -->
    <h2 class="heading abs" style="left:618px;top:34px">ABOUT <strong>US</strong></h2>
    <div class="marker abs" style="left:618px;top:64px"></div>
    <p class="body body--sm abs" style="left:618px;top:82px;width:467px">Here at Ridgeline Throttle we are the creators and the providers of all our motorcycle tours.</p>
    <p class="body body--sm abs" style="left:618px;top:96px;width:467px">With a life-time of experience behind us with riding the roads in the Himalayas our unique motorcycle trips will show you the world's tallest peaks, take you over the other side of the Himalayas into Tibet, explore the tropical southern flatlands, home of the Royal Bengal Tiger and bring you to the birthplace of Buddha.</p>
    <p class="body body--sm abs" style="left:618px;top:129px;width:467px">We have a fleet of Kestrel TR250s , these bikes are light an agile, with a good handful of torque when you need it, perfectly suited to the mountainous terrain. And they are all fitted with ABS plus a digital dash.</p>
    <p class="body body--sm abs" style="left:618px;top:153px;width:467px">Anyone is welcome to sign up to one of our Himalayan motorcycle adventures, no matter what gender, age, ethnicity or belief.</p>
    <h3 class="sub sub--sm abs" style="left:618px;top:169px">Social Work</h3>
    <p class="body body--sm abs" style="left:618px;top:184px;width:467px">Each trip we run helps provide funds for our social projects in Nepal. We currently give to the Asha Devi Science Scholarship Fund, which provides outstanding students from Sindhuli District with tuition and maintenance fees for university in Nepal. Sindhuli District is close to our hearts and we all would like to see this part of Nepal develop and flourish. The scholarship fund is one of the best ways to give young students a chance for further education.</p>

    <div class="member" style="left:664px" role="img" aria-label="Portrait photo of Sujan with a motorbike"></div>
    <p class="member__name" style="left:662px">Sujan</p>
    <p class="bio" style="left:619px">With many journeys on motorbike and on foot with friends and guests across Nepal, travel and adventure run in his blood. His long road background lets him plan smooth routes, welcome guests across the country and solve any problem met on the trail. He puts heart and soul into every ride, so you can rely on him to make your Himalayan trip the best it can be.</p>

    <div class="member" style="left:825px" role="img" aria-label="Portrait photo of Maren in the mountains"></div>
    <p class="member__name" style="left:823px">Maren</p>
    <p class="bio" style="left:780px">will travel with you to make sure your experience is one to remember. Coming from a background in public health, she has lived in Peru, Spain, the Netherlands and Nepal. Raised in the UK and educated abroad, she now works to make your trip a great experience and is your first contact in the UK for help with flights, visas, vaccinations, or simply what to pack, by phone or email.</p>

    <div class="member" style="left:987px" role="img" aria-label="Portrait photo of Hiroki with snowy peaks behind"></div>
    <p class="member__name" style="left:985px">Hiroki</p>
    <p class="bio" style="left:942px">With 30 years of work in the tourism industry he brings a wealth of experience to the team. Having a keen eye for detail, his mechanical skills often save the day, and when not on a motorbike he is driving the support vehicle like a pro. Always friendly and easy going, he is great company and knows Nepal from its architecture to its helicopters!</p>
  </section>

</main>
</body>
</html>
```